Capability statement graphic design documement

We have written a capability statement for our training business, we would like someone to really make it professional and stand out.

Target Market(s)

Engineering, ports and mining companies

Industry/Entity Type

Coal Mining

Font styles to use
Sans Serif

Colors
9bcb3c

Requirements
Must have
• Very good visual designs.
I have included a couple of example such as the TR Harbour capability statement which has good designs.
Our colours are green, black, white, grey. Our logos are uploaded.

```html
<!DOCTYPE html>
<html lang="en">
<head>
<meta charset="utf-8">
<title>SLS Capability Statement – Ethos &amp; Company Details</title>
<link rel="stylesheet" href="https://fonts.googleapis.com/css2?family=Open+Sans:wght@400;600;700&display=swap">
<style>
  :root {
    --brand-green: #9bcb3c;
    --label-green: #8bc04a;
    --deep-green: #1a9a3a;
    --text-grey: #3d3d3d;
    --row-grey: #f1f1f1;
    --rule-blue: #5b5fa8;
    --frame-grey: #6b6b6b;
    --paper: #ffffff;
    --sunset-gold: #f6c65a;
    --sunset-amber: #e9a45a;
    --sunset-rust: #c97a4e;
    --ethos-panel: rgba(236, 234, 178, 0.82);
  }
  * { margin: 0; padding: 0; box-sizing: border-box; }
  html, body { width: 1200px; height: 849px; overflow: hidden; background: var(--paper); }
  body { font-family: "Open Sans", sans-serif; color: var(--text-grey); }

  .spread { position: relative; width: 1200px; height: 849px; overflow: hidden; background: var(--paper); }

  /* Left page */
  .page-left { position: absolute; left: 0; top: 0; width: 600px; height: 849px; }
  .hero-visual {
    position: absolute; inset: 0;
    background:
      radial-gradient(ellipse 260px 320px at 0% 48%, #fff6c8 0%, rgba(255,240,170,0) 70%),
      linear-gradient(180deg, var(--sunset-amber) 0%, var(--sunset-gold) 35%, #f3c063 60%, var(--sunset-rust) 100%);
  }
  .ethos-card {
    position: absolute; left: 177px; top: 126px; width: 256px; height: 408px;
    background: var(--ethos-panel);
    border: 1px solid var(--deep-green); border-radius: 10px;
    padding: 34px 15px 0 15px;
  }
  .ethos-title {
    text-align: center; color: var(--deep-green);
    font-size: 14.5px; font-weight: 600; margin-bottom: 12px;
  }
  .ethos-body { font-size: 11.2px; line-height: 27.2px; color: var(--text-grey); }

  .page-divider { position: absolute; left: 600px; top: 0; width: 1px; height: 849px; background: #d0d0d0; }

  /* Right page */
  .page-right { position: absolute; left: 601px; top: 0; width: 599px; height: 849px; }
  .corner-accent { position: absolute; right: 0; top: 0; }
  .running-head {
    position: absolute; left: 395px; top: 24px;
    color: var(--deep-green); font-size: 9.5px; font-weight: 700; white-space: nowrap;
  }
  .section-title { position: absolute; left: 92px; top: 100px; font-size: 14.5px; font-weight: 400; color: var(--text-grey); }

  .contact-table {
    position: absolute; left: 92px; top: 151px; width: 421px;
    border-collapse: collapse; border: 1px solid var(--frame-grey);
    font-size: 9.2px;
  }
  .contact-table caption, .contact-table .table-head th {
    color: var(--deep-green); font-size: 12.5px; font-weight: 400; height: 21px; text-align: center;
    border-bottom: 1px solid var(--frame-grey); background: var(--paper);
  }
  .contact-table td, .contact-table th.row-label { height: 20.6px; border-bottom: 1px solid var(--rule-blue); }
  .contact-table tr:last-child td, .contact-table tr:last-child th { border-bottom: none; }
  .row-label {
    width: 97px; background: var(--label-green); color: var(--deep-green);
    font-weight: 700; text-align: left; padding-left: 8px;
  }
  .row-value { background: var(--row-grey); padding-left: 41px; color: var(--text-grey); }

  .site-photo {
    position: absolute; left: 94px; top: 413px; width: 468px; height: 307px;
    background: linear-gradient(180deg, #8fb4e0 0%, #c9dcef 25%, #4f7a3e 45%, #6e8f5a 65%, #b9b4a6 85%, #cfcac0 100%);
  }
</style>
</head>
<body>
<main class="spread">
  <section class="page-left">
    <div class="hero-visual" role="img" aria-label="Crane hook and rigging silhouetted against a golden sunset sky"></div>
    <article class="ethos-card">
      <h2 class="ethos-title">Our Ethos</h2>
      <p class="ethos-body">We align ourselves with enlightened management philosophy, regarding people as our major assets and working always at maintaining the highest possible level of communication and interpersonal relations. Our management team is caring and future oriented and our planning and programming soundly organised yet flexible. Our Compan’s commitment to its ethos guarantees our consistently giving of our best in any project we undertake.</p>
    </article>
  </section>

  <div class="page-divider"></div>

  <section class="page-right">
    <svg class="corner-accent" width="110" height="80" viewBox="0 0 110 80" aria-hidden="true">
      <defs>
        <linearGradient id="accentFill" x1="0" y1="0" x2="1" y2="1">
          <stop offset="0" stop-color="#8cc63f"/>
          <stop offset="1" stop-color="#cfe59a"/>
        </linearGradient>
      </defs>
      <path d="M6 0 A 110 110 0 0 0 110 77 L110 0 Z" fill="#e3efc6"/>
      <path d="M10 0 A 104 104 0 0 0 110 72 L110 0 Z" fill="url(#accentFill)"/>
      <path d="M24 28 L110 28 L110 36 L18 36 Z" fill="var(--deep-green)"/>
    </svg>
    <div class="running-head">SLS Capability Statement</div>

    <h1 class="section-title">Company Details</h1>

    <table class="contact-table">
      <thead>
        <tr class="table-head"><th colspan="2">Contact Details</th></tr>
      </thead>
      <tbody>
        <tr><th class="row-label">Company Name</th><td class="row-value">Summit Lift Skills Pty Ltd</td></tr>
        <tr><th class="row-label">ABN</th><td class="row-value">12 345 678 901</td></tr>
        <tr><th class="row-label">CAN</th><td class="row-value">345 678 901</td></tr>
        <tr><th class="row-label">Telephone</th><td class="row-value">0400 123 456</td></tr>
        <tr><th class="row-label">Email</th><td class="row-value">office@summitliftskills.com.au</td></tr>
        <tr><th class="row-label">Website</th><td class="row-value">www.summitliftskills.com.au</td></tr>
        <tr><th class="row-label">Office/Facility</th><td class="row-value">12 Quay Street, Bayview Harbour, QLD 4700</td></tr>
        <tr><th class="row-label">Contact</th><td class="row-value">Dana Whitfield (Business Manager)</td></tr>
      </tbody>
    </table>

    <div class="site-photo" role="img" aria-label="Training yard with a boom lift beside a red steel training structure under blue sky"></div>
  </section>
</main>
</body>
</html>
```